Real Estate 2015 sold listings postcard

Real estate. I want one side to list 2015 sales. Mailing side with additional information. I am including a "concept" but it needs to be professionalized... Feel free to change color, fonts, layout, add watermark, whatever you think will work. Text on backside may be tweaked. I do want postcards addressed. How do i send mailing list or does Brightmark Press do that part?

NOTE: Postcard should be 8.5 x 5.5 inches.
Updates

postcard should be 8.5" x 5.5" size

Target Market(s)

Home owners who may want to sell

Industry/Entity Type

Real Estate Agent

Requirements
Must have
• The sold information and contact oinformation I have provided
Nice to have
• Watermark with my initials

```html
<!DOCTYPE html>
<html lang="en">
<head>
<meta charset="utf-8">
<title>2015 Sales Postcard</title>
<link href="https://fonts.googleapis.com/css2?family=Oswald:wght@300;500;700&family=Open+Sans:wdth,wght@75,400;75,600;100,400;100,600;100,700&family=Dancing+Script:wght@600&display=swap" rel="stylesheet">
<style>
:root{
  --backdrop:#766858;
  --gold:#d4a013;
  --black:#0b0b0b;
  --blue:#1c5aa8;
  --blue-deep:#123f80;
  --red:#e0222b;
  --row-alt:#e6e6e6;
  --white:#ffffff;
  --ink:#222;
}
*{box-sizing:border-box;margin:0;padding:0}
html,body{width:952px;height:1200px;overflow:hidden;background:var(--backdrop);font-family:"Open Sans",sans-serif;color:var(--ink)}
.card{position:absolute;left:93px;width:762px;box-shadow:0 4px 8px rgba(0,0,0,.45);overflow:hidden}
.front{top:83px;height:493px;background:var(--white)}
.back{top:617px;height:493px;background:var(--gold)}

/* front */
.front-header{position:absolute;left:0;top:0;width:100%;height:45px;background:var(--gold)}
.front-title{position:absolute;left:25px;top:5px;font-family:"Oswald",sans-serif;font-weight:700;font-size:28px;color:var(--white);letter-spacing:.3px;text-shadow:1px 1px 1px rgba(0,0,0,.4)}
.front-sold{position:absolute;right:14px;top:6px;font-family:"Oswald",sans-serif;font-weight:300;font-size:28px;color:var(--white)}
.sales{position:absolute;left:0;top:45px;width:762px;border-collapse:collapse;table-layout:fixed;font-size:11.5px}
.sales th{background:var(--black);color:var(--white);height:22px;font-weight:600;font-size:13px;text-align:left;padding-left:8px;border-right:1px solid #555}
.sales td{height:18px;padding-left:8px;border-right:1px solid #bbb;white-space:nowrap}
.sales tbody tr:first-child td{padding-top:6px;height:24px}
.sales tbody tr:nth-child(even) td{background:var(--row-alt)}
.sales .c{text-align:center;padding-left:0}
.sales td.lot-a{border-right:none}

.agent-tag{position:absolute;left:24px;top:369px;width:173px;height:108px;background:var(--gold);border:2px solid #f0c64a;color:var(--white);font-size:9px;font-stretch:75%;white-space:nowrap}
.agent-photo{position:absolute;border-radius:6px;background:linear-gradient(160deg,#c9b090,#b0282c 70%,#7a1a1e)}
.agent-tag .agent-photo{left:5px;top:5px;width:70px;height:95px;border:2px solid #f3d36b}
.agent-tag .name{position:absolute;left:82px;top:4px;font-family:"Oswald",sans-serif;font-weight:500;font-size:14px}
.agent-tag .role{position:absolute;left:82px;top:27px}
.agent-tag .lic{position:absolute;left:82px;top:47px;line-height:13px}
.agent-tag .contact{position:absolute;left:84px;top:77px}
.agent-tag .phone{position:absolute;left:82px;top:87px;font-weight:700;font-size:13px;font-stretch:100%}

.brand-mark{position:absolute;left:462px;top:410px;display:flex;align-items:center;gap:8px;font-family:"Oswald",sans-serif;font-weight:700;font-size:22px;color:var(--black);letter-spacing:1px}
.brand-mark .dot{width:16px;height:16px;background:var(--gold)}

.front-band{position:absolute;left:0;top:451px;width:762px;height:42px}
.front-email{position:absolute;left:229px;top:462px;color:var(--white);font-size:15px;white-space:nowrap}
.front-web{position:absolute;left:434px;top:462px;color:var(--white);font-size:15px;font-weight:700;white-space:nowrap}
.front-note{position:absolute;left:618px;top:458px;width:138px;color:var(--white);font-size:6.2px;line-height:8.5px}
.sep{position:absolute;top:460px;width:1px;height:22px;background:rgba(255,255,255,.6)}

/* back */
.back-header{position:absolute;left:0;top:0;width:100%;height:67px;background:var(--black)}
.back-header h2{position:absolute;left:30px;top:14px;font-family:"Oswald",sans-serif;font-weight:700;font-size:29px;color:var(--white);letter-spacing:.2px}
.offer-band{position:absolute;left:0;top:67px;width:100%;height:126px;background:linear-gradient(180deg,var(--blue),var(--blue-deep));border:2px dashed var(--white)}
.agent-card{position:absolute;left:31px;top:57px;width:257px;height:146px;background:var(--white);box-shadow:0 2px 4px rgba(0,0,0,.4);white-space:nowrap}
.agent-card .red{position:absolute;left:4px;top:0;width:249px;height:126px;background:linear-gradient(90deg,#c81820,var(--red))}
.agent-card .agent-photo{left:10px;top:0;width:97px;height:120px;border-radius:0}
.agent-card .name{position:absolute;left:119px;top:8px;color:var(--white);font-weight:700;font-size:15.5px}
.agent-card .role{position:absolute;left:119px;top:33px;color:var(--white);font-size:11.5px}
.agent-card .lic{position:absolute;left:119px;top:62px;color:var(--white);font-size:13.5px}
.agent-card .phone{position:absolute;left:119px;top:95px;color:var(--white);font-family:"Oswald",sans-serif;font-weight:500;font-size:21px;line-height:26px}
.agent-card .mail{position:absolute;left:11px;top:131px;font-size:9px;font-weight:600}
.agent-card .web{position:absolute;left:134px;top:129px;font-size:11.5px;font-weight:700}
.headline{position:absolute;left:308px;top:80px;font-family:"Oswald",sans-serif;font-weight:700;color:var(--white);line-height:50px;text-shadow:2px 2px 2px rgba(0,0,0,.4)}
.headline .l1{font-size:47px;display:block}
.headline .l2{font-size:40px;display:block;line-height:44px}
.callout{position:absolute;left:605px;top:73px;width:130px;height:110px;background:var(--white);border:1px solid #ccc;font-family:"Dancing Script",cursive;font-weight:600;font-size:19px;line-height:25px;text-align:center;padding-top:5px;color:#222}
.listing-title{position:absolute;left:50px;top:216px;font-family:"Oswald",sans-serif;font-weight:700;font-size:25px;line-height:31px;color:var(--white);text-shadow:1px 2px 2px rgba(0,0,0,.35)}
.copy{position:absolute;left:50px;top:283px;width:376px;color:var(--white);font-size:11.2px;line-height:16.2px;text-align:justify}
.copy p+p{margin-top:10px}
.address-box{position:absolute;left:467px;top:309px;width:263px;height:154px;background:var(--white);border-radius:10px;box-shadow:0 2px 4px rgba(0,0,0,.3)}
.address-box span{position:absolute;left:12px;width:236px;height:1px;background:#aaa}
.back-foot{position:absolute;left:0;bottom:0;width:100%;height:14px;background:linear-gradient(90deg,var(--blue-deep),#3a86d6 50%,var(--blue-deep))}
</style>
</head>
<body>

<section class="card front">
  <div class="front-header">
    <h1 class="front-title">2015 SALES IN YOUR NEIGHBORHOOD</h1>
    <div class="front-sold">SOLD</div>
  </div>

  <table class="sales">
    <colgroup><col style="width:160px"><col style="width:43px"><col style="width:54px"><col style="width:53px"><col style="width:70px"><col style="width:70px"><col style="width:82px"><col style="width:81px"><col style="width:67px"><col style="width:82px"></colgroup>
    <thead><tr><th>Address</th><th>BR</th><th>BA</th><th>Sq Ft</th><th colspan="2" style="text-align:center">Lot Size</th><th>List Price</th><th>Sale Price</th><th>$/Sq. Ft</th><th class="c">DOM</th></tr></thead>
    <tbody>
      <tr><td>387 Alder PL*</td><td class="c">3</td><td>3 1/2</td><td></td><td class="lot-a">2588</td><td>9239</td><td>3088000</td><td>3,100,000</td><td>1198</td><td class="c">9</td></tr>
      <tr><td>3657 Birch ST</td><td class="c">4</td><td>3</td><td></td><td class="lot-a">2228</td><td>6147</td><td>2998000</td><td>3000000</td><td>1346</td><td class="c">23</td></tr>
      <tr><td>261 Brookview DR</td><td class="c">4</td><td>3</td><td></td><td class="lot-a">2185</td><td>7040</td><td>2500000</td><td>2925000</td><td>1,339</td><td class="c">9</td></tr>
      <tr><td>437 Fernwood AVE*</td><td class="c">4</td><td>2</td><td></td><td class="lot-a">1611</td><td>13,237</td><td>2498000</td><td>2610000</td><td>1620</td><td class="c">8</td></tr>
      <tr><td>4123 Drake AVE*</td><td class="c">4</td><td>2</td><td></td><td class="lot-a">2227</td><td>8700</td><td>2295000</td><td>2595000</td><td>1165</td><td class="c">8</td></tr>
      <tr><td>76 Ridgeview CIR *</td><td class="c">3</td><td>2</td><td></td><td class="lot-a">1364</td><td>5917</td><td>1788000</td><td>2525000</td><td>1851</td><td class="c">8</td></tr>
      <tr><td>3665 Ravenna CIR</td><td class="c">4</td><td>2</td><td></td><td class="lot-a">1646</td><td>6404</td><td>2500000</td><td>2475000</td><td>1504</td><td class="c">18</td></tr>
      <tr><td>410 Amber PL *</td><td class="c">3</td><td>2</td><td></td><td class="lot-a">1674</td><td>11200</td><td>2498000</td><td>2450000</td><td>1464</td><td class="c">16</td></tr>
      <tr><td>291 Brookview DR*</td><td class="c">4</td><td>2</td><td></td><td class="lot-a">1690</td><td>8178</td><td>2199000</td><td>2400000</td><td>1420</td><td class="c">7</td></tr>
      <tr><td>303 Brookview DR.</td><td class="c">3</td><td>2</td><td></td><td class="lot-a">1674</td><td>8538</td><td>2200000</td><td>2260000</td><td>1350</td><td class="c">97</td></tr>
      <tr><td>93 Ridgeview CIR</td><td class="c">3</td><td>2</td><td></td><td class="lot-a">1243</td><td>6080</td><td>1488000</td><td>2250000</td><td>1810</td><td class="c">7</td></tr>
      <tr><td>3702 Carrow CIR *</td><td class="c">4</td><td>2</td><td></td><td class="lot-a">1333</td><td>6493</td><td>1895000</td><td>2227500</td><td>1671</td><td class="c">6</td></tr>
      <tr><td>372 Parkhill DR *</td><td class="c">3</td><td>2</td><td></td><td class="lot-a">1740</td><td>6324</td><td>2200000</td><td>2180000</td><td>1,253</td><td class="c">12</td></tr>
      <tr><td>3647 Birch ST</td><td class="c">4</td><td>2</td><td></td><td class="lot-a">1474</td><td>6111</td><td>1799900</td><td>2115000</td><td>1,435</td><td class="c">17</td></tr>
      <tr><td>60 Ridgeview Cir</td><td class="c">4</td><td>2</td><td></td><td class="lot-a">1456</td><td>6111</td><td>1788000</td><td>2000000</td><td>1374</td><td class="c">11</td></tr>
      <tr><td>252 Fairhaven CT</td><td class="c">3</td><td>2</td><td></td><td class="lot-a">1428</td><td>10,624</td><td>1,950,000</td><td>2,100,000</td><td>1471</td><td class="c">20</td></tr>
    </tbody>
  </table>

  <svg class="front-band" viewBox="0 0 762 42" preserveAspectRatio="none" aria-hidden="true">
    <defs><linearGradient id="bandGrad" x1="0" x2="1"><stop offset="0" stop-color="#3a86d6"/><stop offset="1" stop-color="#123f80"/></linearGradient></defs>
    <polygon points="0,42 0,26 200,26 228,0 762,0 762,42" fill="url(#bandGrad)"/>
  </svg>

  <div class="agent-tag">
    <div class="agent-photo" role="img" aria-label="Portrait photo of the agent"></div>
    <div class="name">Dana Whitfield</div>
    <div class="role">Relocation Specialist</div>
    <div class="lic">California License:<br>#01234567</div>
    <div class="contact">Contact me:</div>
    <div class="phone">650-555-0162</div>
  </div>

  <div class="brand-mark"><span class="dot"></span>HARBORLINE REALTY</div>

  <div class="front-email">email: dwhitfield@hlr.com</div>
  <div class="sep" style="left:424px"></div>
  <div class="front-web">www.DWhitfield.com</div>
  <div class="sep" style="left:608px"></div>
  <div class="front-note">* indicates Harborline Realty listing or sale. This information is deemed reliable, but not verified or guaranteed.</div>
</section>

<section class="card back">
  <div class="back-header"><h2>Traditionally, Feb. through April are the best months to sell</h2></div>
  <div class="offer-band"></div>

  <div class="agent-card">
    <div class="red"></div>
    <div class="agent-photo" role="img" aria-label="Portrait photo of the agent"></div>
    <div class="name">Dana Whitfield</div>
    <div class="role">Relocation Specialist</div>
    <div class="lic">License: #01234567</div>
    <div class="phone">650-555-0162</div>
    <div class="mail">email: dwhitfield@hlr.com</div>
    <div class="web">www.DWhitfield.com</div>
  </div>

  <div class="headline"><span class="l1">MOST OFFERS</span><span class="l2">HIGHEST PRICES</span></div>
  <div class="callout">Don't Wait.<br>Call Now for<br>a Private<br>Consultation!</div>

  <h3 class="listing-title">Our Listings are advertised locally<br>and in 40 countries!!</h3>
  <div class="copy">
    <p>Our market continues to be strong, which reflects both our vibrant and growing local economy and our seemingly chronic shortage of inventory. As long as those conditions continue, our market values will remain high. That is good news to sellers who may want to down-size or move to a different area for a new job, or maybe to be closer to family.</p>
    <p>I am a Harborline Realty certified Relocation Specialist, and, as such, I can connect you with experienced and professional real estate agent anywhere in the country and in most countries around the world. We can co-ordinate your transactions at both ends, making your transition as seamless as possible. If you are planning a move, across the street or across the county, call me now for a confidential consultation.</p>
  </div>

  <div class="address-box">
    <span style="top:42px"></span><span style="top:75px"></span><span style="top:108px"></span><span style="top:141px"></span>
  </div>
  <div class="back-foot"></div>
</section>

</body>
</html>
```